Whole Body Cryotherapy Brochure Design Project

We need a tri-fold brochure design for our new Whole Body Cryotherapy chamber in San Antonio, TX. The WBC chamber is the first available to the public in the area. WBC has many benefits including, but not limited to reduce swelling & inflammation, whole body recovery, pain relief, sports enhancement, anti-aging & metabolic boost. We created an "unprofessional" brochure with as much information as we could possibly fit. This "professional" brochure should be eye catching, clean & modern & simple. We would also like the brochure to have pricing & Introductory coupon. We've attached the "unprofessional" brochure we created & also the window sign & poster we had "professionally" created along with our logo (blue & black; either layout).

Requirements
Must have
• Princing:
Single Session $75
3 Session Package $195
6 Session Package $360
9 Session Package $495
12 Session Package $600
Discounts for Holloway Joint & Motion patients, Ironpulse, members of the military & service personnel.
Packages can be shared.
Payment plans are available.
Large Group discounts are also available.

Coupon:
Introductory Session (for new WBC clients only)
$45 (Regular Price $75)

```html
<!DOCTYPE html>
<html lang="en">
<head>
<meta charset="utf-8">
<title>Holloway Joint &amp; Motion — Cryotherapy Spread</title>
<link rel="stylesheet" href="https://fonts.googleapis.com/css2?family=Exo+2:wght@300;400;600&family=Open+Sans:wght@400;600;700&display=swap">
<style>
  :root {
    --backdrop: #e6e3de;
    --paper: #ffffff;
    --brand-blue: #1a6fb0;
    --deep-blue: #0d5a99;
    --heading-grey: #8a8d90;
    --services-grey: #6e8ea8;
    --body-text: #5b5f63;
    --rule: #c9cdd1;
    --sky-top: #1d3f9a;
    --sky-low: #6f8fc4;
    --grass: #3f6b3a;
    --skin: #cfa89a;
    --studio: #d9d6d2;
    --xray-dark: #1b3f8f;
    --xray-light: #5d8fd8;
  }
  * { box-sizing: border-box; margin: 0; padding: 0; }
  html, body {
    width: 1200px; height: 804px; overflow: hidden;
    background: var(--backdrop);
    font-family: "Open Sans", Arial, sans-serif;
  }
  .spread {
    position: absolute; left: 20px; top: 22px;
    width: 1160px; height: 760px;
    display: flex;
    box-shadow: 0 2px 10px rgba(0,0,0,.12);
  }
  .page {
    position: relative; width: 580px; height: 760px;
    background: var(--paper); overflow: hidden;
  }
  .page--left { border-right: 1px solid #e4e4e4; }

  /* ---------- left page ---------- */
  .hero-photo {
    position: absolute; left: 0; top: 0; width: 580px; height: 380px;
    background: linear-gradient(180deg, var(--sky-top) 0%, var(--sky-low) 50%, var(--grass) 68%, var(--grass) 100%);
  }
  .hero-wave { position: absolute; left: 0; top: 0; width: 580px; height: 380px; }
  .mission-title {
    position: absolute; left: 40px; top: 370px;
    font-family: "Exo 2", Arial, sans-serif; font-weight: 300; font-size: 42px;
    line-height: 1; color: var(--heading-grey); letter-spacing: .5px;
  }
  .mission-title strong { font-weight: 400; color: var(--brand-blue); }
  .mission-kicker {
    position: absolute; left: 136px; top: 420px;
    font-size: 8px; font-weight: 700; letter-spacing: 2px; color: var(--brand-blue);
  }
  .mission-rule {
    position: absolute; left: 40px; top: 440px; width: 240px;
    border-top: 1px dotted var(--rule);
  }
  .detail-photo {
    position: absolute; left: 40px; top: 462px; width: 250px; height: 130px;
    background: linear-gradient(135deg, #8a6d66 0%, var(--skin) 55%, #efe2dc 100%);
  }
  .detail-wave { position: absolute; left: 40px; top: 540px; width: 250px; height: 62px; }

  .coupon {
    position: absolute; left: 40px; top: 618px; width: 250px;
    border: 1px dashed var(--brand-blue); padding: 9px 12px;
    color: var(--body-text);
  }
  .coupon__label {
    font-size: 8px; font-weight: 700; letter-spacing: 1.6px;
    color: var(--brand-blue); text-transform: uppercase;
  }
  .coupon__row { display: flex; align-items: baseline; gap: 10px; margin-top: 3px; }
  .coupon__price {
    font-family: "Exo 2", Arial, sans-serif; font-size: 30px; font-weight: 400;
    line-height: 1; color: var(--brand-blue);
  }
  .coupon__regular { font-size: 9px; line-height: 1.4; }
  .coupon__note { font-size: 8px; margin-top: 3px; }

  .pricing {
    position: absolute; left: 318px; top: 300px; width: 232px;
    color: var(--body-text);
  }
  .pricing__title {
    font-size: 8.5px; font-weight: 700; letter-spacing: 1.4px;
    color: var(--brand-blue); text-transform: uppercase; margin-bottom: 10px;
  }
  .price-list { list-style: none; }
  .price-list__item {
    display: flex; align-items: baseline; gap: 6px;
    font-size: 10px; line-height: 1; padding: 6px 0;
  }
  .price-list__item::after { content: none; }
  .price-list__name { white-space: nowrap; }
  .price-list__dots { flex: 1; border-bottom: 1px dotted var(--rule); transform: translateY(-3px); }
  .price-list__amount { font-weight: 700; color: var(--brand-blue); }
  .pricing__notes { margin-top: 14px; font-size: 9.5px; line-height: 1.7; }
  .pricing__notes p + p { margin-top: 6px; }

  .folio {
    position: absolute; bottom: 22px;
    display: flex; align-items: center; gap: 8px;
    font-size: 8px; color: var(--brand-blue); letter-spacing: .3px;
  }
  .folio__mark { width: 9px; height: 9px; background: var(--brand-blue); }
  .page--left .folio { left: 40px; }
  .page--right .folio { right: 24px; flex-direction: row-reverse; }

  /* ---------- right page ---------- */
  .brand {
    position: absolute; right: 30px; top: 20px;
    display: flex; align-items: center; gap: 8px;
  }
  .brand__square { width: 16px; height: 16px; background: var(--brand-blue); }
  .brand__name {
    font-size: 12px; font-weight: 700; letter-spacing: 1.5px;
    color: var(--brand-blue); text-transform: uppercase;
  }
  .services-title {
    position: absolute; left: 30px; top: 60px;
    font-family: "Exo 2", Arial, sans-serif; font-weight: 300; font-size: 38px;
    color: var(--services-grey);
  }
  .services-kicker {
    position: absolute; left: 32px; top: 108px;
    font-size: 7.5px; font-weight: 700; letter-spacing: 1.6px; color: var(--brand-blue);
  }
  .services-rule {
    position: absolute; left: 32px; top: 124px; width: 300px;
    border-top: 1px dotted var(--rule);
  }
  .service-list { position: absolute; left: 34px; top: 150px; width: 290px; list-style: none; }
  .service { position: relative; padding-left: 26px; margin-bottom: 38px; }
  .service__icon { position: absolute; left: 0; top: 2px; width: 16px; height: 12px; }
  .service__name {
    font-size: 8.5px; font-weight: 700; letter-spacing: 1.3px;
    color: var(--brand-blue); text-transform: uppercase; margin-bottom: 6px;
  }
  .service__text { font-size: 8.5px; line-height: 1.6; color: var(--body-text); }

  .treatment-photo {
    position: absolute; left: 345px; top: 54px; width: 215px; height: 120px;
    background: linear-gradient(160deg, #b08a78 0%, var(--studio) 45%, #f2f0ee 100%);
  }
  .anatomy-panel {
    position: absolute; left: 345px; top: 184px; width: 215px; height: 500px;
    background: radial-gradient(ellipse at 55% 45%, var(--xray-light) 0%, var(--xray-dark) 75%);
  }
</style>
</head>
<body>
<main class="spread">

  <section class="page page--left">
    <div class="hero-photo" role="img" aria-label="Photo of a golfer mid-swing beside a golf cart on a green, with a snowy mountain and blue sky behind"></div>
    <svg class="hero-wave" viewBox="0 0 580 380" preserveAspectRatio="none" aria-hidden="true">
      <path d="M0 352 C 200 326, 420 236, 580 168 L580 380 L0 380 Z" fill="#ffffff"/>
      <path d="M0 338 C 200 312, 420 222, 580 154 L580 168 C 420 236, 200 326, 0 352 Z" fill="#1a6fb0"/>
    </svg>

    <h1 class="mission-title">Our <strong>Mission</strong></h1>
    <p class="mission-kicker">SPORTS CHIROPRACTOR</p>
    <div class="mission-rule"></div>

    <div class="detail-photo" role="img" aria-label="Close-up photo of a steel soft-tissue tool gliding over a patient's shoulder"></div>
    <svg class="detail-wave" viewBox="0 0 250 62" preserveAspectRatio="none" aria-hidden="true">
      <path d="M0 54 C 90 50, 180 26, 250 0 L250 62 L0 62 Z" fill="#ffffff"/>
      <path d="M0 46 C 90 42, 180 18, 250 -8 L250 4 C 180 30, 90 54, 0 58 Z" fill="#1a6fb0"/>
    </svg>

    <div class="coupon">
      <p class="coupon__label">Introductory Session Coupon</p>
      <div class="coupon__row">
        <span class="coupon__price">$45</span>
        <span class="coupon__regular">Regular Price $75</span>
      </div>
      <p class="coupon__note">For new WBC clients only</p>
    </div>

    <div class="pricing">
      <h2 class="pricing__title">Whole Body Cryotherapy Pricing</h2>
      <ul class="price-list">
        <li class="price-list__item"><span class="price-list__name">Single Session</span><span class="price-list__dots"></span><span class="price-list__amount">$75</span></li>
        <li class="price-list__item"><span class="price-list__name">3 Session Package</span><span class="price-list__dots"></span><span class="price-list__amount">$195</span></li>
        <li class="price-list__item"><span class="price-list__name">6 Session Package</span><span class="price-list__dots"></span><span class="price-list__amount">$360</span></li>
        <li class="price-list__item"><span class="price-list__name">9 Session Package</span><span class="price-list__dots"></span><span class="price-list__amount">$495</span></li>
        <li class="price-list__item"><span class="price-list__name">12 Session Package</span><span class="price-list__dots"></span><span class="price-list__amount">$600</span></li>
      </ul>
      <div class="pricing__notes">
        <p>Discounts for Holloway Joint &amp; Motion patients, Ironpulse, members of the military &amp; service personnel.</p>
        <p>Packages can be shared. Payment plans are available. Large group discounts are also available.</p>
      </div>
    </div>

    <footer class="folio"><span class="folio__mark"></span><span>www.hollowayjointmotion.com</span></footer>
  </section>

  <section class="page page--right">
    <div class="brand"><span class="brand__square"></span><span class="brand__name">Holloway Joint &amp; Motion</span></div>

    <h2 class="services-title">Services</h2>
    <p class="services-kicker">NEQUE PORRO QUISQUAM EST QUI DOLOREM IPSUM QUI.</p>
    <div class="services-rule"></div>

    <ul class="service-list">
      <li class="service">
        <svg class="service__icon" viewBox="0 0 16 12" aria-hidden="true"><rect y="0" width="16" height="4" fill="#1a6fb0"/><rect y="7" width="16" height="4" fill="#0d5a99"/></svg>
        <h3 class="service__name">Whole Body Cryotherapy</h3>
        <p class="service__text">Three minutes in the chamber cools the skin fast, easing swelling and inflammation, speeding whole body recovery and leaving you with a lasting lift in energy and mood.</p>
      </li>
      <li class="service">
        <svg class="service__icon" viewBox="0 0 16 12" aria-hidden="true"><rect y="0" width="16" height="4" fill="#1a6fb0"/><rect y="7" width="16" height="4" fill="#0d5a99"/></svg>
        <h3 class="service__name">Corrective Chiropractic</h3>
        <p class="service__text">Gentle, precise adjustments restore alignment and joint motion, easing back and neck pain while helping your body handle training loads and everyday strain with less effort.</p>
      </li>
      <li class="service">
        <svg class="service__icon" viewBox="0 0 16 12" aria-hidden="true"><rect y="0" width="16" height="4" fill="#1a6fb0"/><rect y="7" width="16" height="4" fill="#0d5a99"/></svg>
        <h3 class="service__name">Active Tissue Release</h3>
        <p class="service__text">Targeted pressure and guided movement release scar tissue and adhesions in muscles, tendons and nerves, restoring smooth motion and strength after strain or repeated stress.</p>
      </li>
      <li class="service">
        <svg class="service__icon" viewBox="0 0 16 12" aria-hidden="true"><rect y="0" width="16" height="4" fill="#1a6fb0"/><rect y="7" width="16" height="4" fill="#0d5a99"/></svg>
        <h3 class="service__name">Flex Taping</h3>
        <p class="service__text">Flexible tape supports muscles and joints without limiting range, calming swelling and giving steady feedback so you can keep training while tissues heal.</p>
      </li>
      <li class="service">
        <svg class="service__icon" viewBox="0 0 16 12" aria-hidden="true"><rect y="0" width="16" height="4" fill="#1a6fb0"/><rect y="7" width="16" height="4" fill="#0d5a99"/></svg>
        <h3 class="service__name">Steelform</h3>
        <p class="service__text">Smooth steel tools find and break up stiff, restricted tissue, improving blood flow and flexibility so lingering aches finally settle and movement feels free again.</p>
      </li>
    </ul>

    <div class="treatment-photo" role="img" aria-label="Photo of a chiropractor stretching a patient's arm on a treatment table"></div>
    <div class="anatomy-panel" role="img" aria-label="Illustration of a translucent blue human figure seen from behind, with the spine highlighted in red"></div>

    <footer class="folio"><span class="folio__mark"></span><span>www.hollowayjointmotion.com</span></footer>
  </section>

</main>
</body>
</html>
```